Wedding Photo Studio needs custom webpage

I'm changing up my service offering to offer multiple editing styles. I'm looking to update my website to reflect that but still showcase my dreamy edits as an attention grabbing part of the website.

I will have 4 color editing styles (Colm's Hallmark, Bright & Airy, Silken Oak, Dreamy) and one black and white style. I have attached sample images in each style.

I also attached a couple dreamy edits that can be used as attention grabbing images.

I'm hoping for some functionality that perhaps takes a single image and divides it by 4 to show 25% in each style that can be clicked on and would 'maximize' the carousel to that style but still have a functionality to go to a different style after being maximized.

You can see www.colmvphotography.com for the current design and content. It doesn't have to be too different (but can be). It just needs to showcase the multiple editing styles effectively.

Target Market(s)

Couples who are having $20-50k weddings.

Industry/Entity Type

Photography

Coding

Coded - Design and coding required

Number of Pages Required

3 page

Colors

Designer to choose colors to be used in the design.

Requirements
Must have
• Pricing page with toggles for (off-season/on-season, Saturday/non-saturday) accurate pricing, good way to show multiple editing style photos.

```html
<!DOCTYPE html>
<html lang="en">
<head>
<meta charset="utf-8">
<title>Colm V Photography</title>
<link href="https://fonts.googleapis.com/css2?family=Montserrat:wght@300;400;500;600;700;800&family=Great+Vibes&display=swap" rel="stylesheet">
<style>
:root{
  --blue:#0b4ea2;
  --ink:#1d1d1d;
  --text:#444;
  --muted:#8a8a8a;
  --line:#cfcfcf;
  --dark:#1f1f1f;
  --white:#fff;
}
*{box-sizing:border-box;margin:0;padding:0}
html,body{width:1200px;height:3951px;overflow:hidden;background:var(--white)}
body{position:relative;font-family:'Montserrat',sans-serif;color:var(--ink)}
.abs{position:absolute}
.script{font-family:'Great Vibes',cursive;font-weight:400}

/* header */
.site-header{position:absolute;left:0;top:0;width:1200px;height:62px;background:var(--white)}
.brand{position:absolute;left:80px;top:16px;display:flex;align-items:center;gap:8px;font-size:17px;font-weight:500;color:var(--blue)}
.brand-dot{width:14px;height:14px;border-radius:50%;background:var(--blue)}
.main-nav{position:absolute;left:410px;top:25px;display:flex;align-items:center;gap:18px;font-size:10.5px;color:#555;letter-spacing:.3px}
.main-nav .sep{width:5px;height:5px;border-radius:50%;background:var(--blue)}
.btn-contact{position:absolute;left:992px;top:15px;width:126px;height:33px;background:var(--blue);color:#fff;border-radius:3px;font-size:10.5px;font-weight:600;display:flex;align-items:center;justify-content:center;gap:6px}

/* hero */
.hero{position:absolute;left:0;top:62px;width:1200px;height:608px;background:linear-gradient(160deg,#7a3b1e 0%,#c9743f 30%,#4a2d27 60%,#8f6a58 100%)}
.photo-frame{position:absolute;background:#fff;padding:7px;box-shadow:0 6px 18px rgba(0,0,0,.25)}
.photo-frame .ph{width:100%;height:100%}
.arrow{position:absolute;width:44px;height:44px;border-radius:50%;background:var(--blue);display:flex;align-items:center;justify-content:center}
.hero-script{position:absolute;left:188px;top:455px;font-size:46px;color:#fff}
.hero-city{position:absolute;left:188px;top:512px;font-size:34px;font-weight:400;color:#fff;letter-spacing:.5px}

/* about */
.about-photo{position:absolute;left:187px;top:783px;width:403px;height:443px;background:linear-gradient(150deg,#6b5a45,#b9a58a 55%,#4a3c30)}
.tape{position:absolute;left:150px;top:775px;width:125px;height:48px;background:var(--blue);transform:rotate(-35deg)}
.section-title{font-size:34px;font-weight:400;color:var(--ink);letter-spacing:.5px}
.about-copy{position:absolute;left:643px;top:900px;width:360px;font-size:10px;line-height:15.5px;color:var(--text)}
.signature{position:absolute;left:905px;top:985px;font-size:36px;color:var(--blue);transform:rotate(-8deg)}
.serving-title{position:absolute;left:643px;top:1058px;font-size:16px;font-weight:400}
.serving-list{position:absolute;left:643px;top:1096px;width:380px;display:flex;flex-wrap:wrap;row-gap:18px;column-gap:30px;font-size:10px;font-weight:600;color:#333;list-style:none}
.serving-list li{display:flex;align-items:center;gap:8px;height:12px}
.serving-list li::before{content:"";width:5px;height:5px;border-radius:50%;background:var(--blue)}

/* styles grid */
.style-tile{position:absolute;width:582px;height:344px}
.style-label{position:absolute;left:50%;top:0;transform:translateX(-50%);width:240px;height:46px;background:var(--dark);color:#fff;font-size:17px;font-weight:800;display:flex;align-items:center;justify-content:center;letter-spacing:.3px}
.style-badge{position:absolute;left:546px;top:1624px;width:108px;height:108px;border-radius:50%;background:var(--dark)}

/* testimonials */
.testi-card{position:absolute;top:2220px;height:180px;border:1px solid var(--line);background:#fff;padding:38px 50px 0;text-align:center;font-size:10px;line-height:15px;color:var(--text)}
.testi-card .who{display:block;margin-top:12px;font-weight:700;color:var(--blue);font-size:10px}
.quote-dot{position:absolute;width:36px;height:36px;border-radius:50%;background:var(--blue);display:flex;align-items:center;justify-content:center;color:#fff;font-weight:800;font-size:20px}
.avatar{position:absolute;width:34px;height:34px;border-radius:50%;border:2px solid #fff;box-shadow:0 0 0 1px #ddd}
.dots{position:absolute;left:548px;top:2463px;display:flex;gap:12px}
.dots span{width:7px;height:7px;border-radius:50%;background:#cfd6e2}
.dots span.on{background:var(--blue)}

/* dreamy */
.dreamy{position:absolute;left:0;top:2556px;width:1200px;height:606px;background:linear-gradient(110deg,#d8b59c 0%,#f0d9c2 35%,#c79a78 65%,#e7cdb7 100%)}
.dreamy-script{position:absolute;left:963px;top:3020px;font-size:38px;color:var(--blue)}
.dreamy-title{position:absolute;left:968px;top:3076px;font-size:34px;color:var(--ink);letter-spacing:1px}

/* blogs */
.blog-main-img{position:absolute;left:187px;top:3327px;width:403px;height:228px;background:linear-gradient(160deg,#3a2410,#c98a34 50%,#2b1a0d)}
.date{font-size:9.5px;font-weight:600;color:var(--blue)}
.blog-title{font-size:19px;font-weight:400;line-height:24px;color:var(--ink)}
.read-more{font-size:9.5px;font-weight:700;color:var(--blue);text-decoration:underline}
.blog-item{position:absolute;left:609px;width:420px;height:108px}
.blog-item .thumb{position:absolute;left:0;top:0;width:122px;height:108px}
.blog-item .info{position:absolute;left:141px;top:0}
.blog-item .blog-title{font-size:17px;line-height:21px;margin:6px 0 10px}

/* footer */
.site-footer{position:absolute;left:0;top:3895px;width:1200px;height:56px;background:#232323;color:#fff}
.site-footer p{position:absolute;left:187px;top:22px;font-size:10.5px}
.social{position:absolute;top:17px;width:24px;height:24px;border-radius:50%}
</style>
</head>
<body>

<header class="site-header">
  <div class="brand"><span class="brand-dot"></span>Colm V</div>
  <nav class="main-nav">
    <span>HOME</span><span class="sep"></span><span>THE TEAM</span><span class="sep"></span><span>PORTFOLIO</span><span class="sep"></span><span>BLOG</span><span class="sep"></span><span>PRICING</span>
  </nav>
  <div class="btn-contact">
    <svg width="10" height="10" viewBox="0 0 24 24"><path fill="#fff" d="M6.6 10.8a15 15 0 0 0 6.6 6.6l2.2-2.2c.3-.3.7-.4 1-.2 1.1.4 2.3.6 3.6.6.6 0 1 .4 1 1V20c0 .6-.4 1-1 1A17 17 0 0 1 3 4c0-.6.4-1 1-1h3.5c.6 0 1 .4 1 1 0 1.3.2 2.5.6 3.6.1.3 0 .7-.2 1z"/></svg>
    Contact Me
  </div>
</header>

<section class="hero">
  <div class="abs" role="img" aria-label="Couple dancing under a lit modern canopy at night" style="left:0;top:0;width:1200px;height:608px"></div>
  <div class="photo-frame" style="left:675px;top:50px;width:343px;height:509px">
    <div class="ph" role="img" aria-label="Black and white portrait of a bride and groom on stone steps" style="background:linear-gradient(160deg,#2d2d2d,#9a9a9a 50%,#e4e4e4)"></div>
  </div>
  <div class="arrow" style="left:38px;top:282px"><svg width="12" height="12" viewBox="0 0 10 10"><path d="M7 1 2 5l5 4z" fill="#fff"/></svg></div>
  <div class="arrow" style="left:1118px;top:282px"><svg width="12" height="12" viewBox="0 0 10 10"><path d="M3 1l5 4-5 4z" fill="#fff"/></svg></div>
  <div class="hero-script script">Wedding Photographer</div>
  <div class="hero-city">KITCHENER-WATERLOO</div>
</section>

<section class="about">
  <div class="about-photo" role="img" aria-label="Bride and groom portrait beside a stone wall in autumn"></div>
  <div class="tape"></div>
  <h2 class="section-title abs" style="left:643px;top:838px">ABOUT ME</h2>
  <p class="about-copy">I am an accountant by day, photographer by night. I once read a happy life is had by loving your job, loving your creative hobby and the love of family; photography is one part of that for me. I focus primarily on wedding photography in southern Ontario. I cover Toronto, Hamilton, Kitchener, Waterloo, London and anywhere in the world you want to send me. If you like what I do, please reach out, I'm happy to meet with you and chat more about your big day.</p>
  <div class="signature script">Colm Vance</div>
  <h3 class="serving-title">ALSO SERVING</h3>
  <ul class="serving-list">
    <li>Toronto</li><li>Hamilton</li><li>London</li><li>Niagara</li>
    <li>Cambridge</li><li>Mississauga</li><li>Brampton</li><li>Guelph</li>
    <li>Burlington</li>
  </ul>
</section>

<section class="styles">
  <div class="style-tile" role="img" aria-label="Black and white portrait of a groom" style="left:12px;top:1335px;background:linear-gradient(135deg,#3a3a3a,#bdbdbd 55%,#5a5a5a)"><div class="style-label">BLACK &amp; WHITE</div></div>
  <div class="style-tile" role="img" aria-label="Bright and airy portrait of a bride among greenery" style="left:606px;top:1335px;background:linear-gradient(135deg,#8aa36a,#dcd6c4 50%,#6f8a4d)"><div class="style-label">BRIGHT &amp; AIRY</div></div>
  <div class="style-tile" role="img" aria-label="Couple holding hands on a garden path" style="left:12px;top:1690px;background:linear-gradient(135deg,#6f5c4a,#b5a895 50%,#d9cbbd)"><div class="style-label">COLM'S HALLMARK</div></div>
  <div class="style-tile" role="img" aria-label="Bride holding a bouquet in warm brown tones" style="left:606px;top:1690px;background:linear-gradient(135deg,#cdbfb2,#a07c63 55%,#5e3f2c)"><div class="style-label">SILKEN OAK</div></div>
  <div class="style-badge"></div>
</section>

<section class="testimonials">
  <h2 class="section-title abs" style="left:0;width:1200px;text-align:center;top:2118px">TESTIMONIALS</h2>

  <div class="testi-card" style="left:-238px;width:546px">Our wedding photos! We got so so much more for so so much less than expected and then some. I recommend him 100 times over!<span class="who">Owen &amp; Lara</span></div>
  <div class="quote-dot" style="left:18px;top:2202px">"</div>
  <div class="avatar" style="left:18px;top:2383px;background:#c8b7a6"></div>

  <div class="testi-card" style="left:328px;width:544px">Colm is the absolute best! He did a SPECTACULAR job with our wedding photos. He got images of everything, even the things that we never thought he would notice. Hands down Colm is the best photographer I have seen in the area and you will not be disappointed.<span class="who">Remy &amp; Alina</span></div>
  <div class="quote-dot" style="left:582px;top:2202px">"</div>
  <div class="avatar" style="left:583px;top:2383px;background:#b3736b"></div>

  <div class="testi-card" style="left:892px;width:546px;text-align:left;padding-left:30px">We got married September 30 and hired Colm and we were AMAZING job!! He is very professional, very organized, got all the most important moments in such beautiful light, the amazing photos from our wedding would very much make photographer and his prices are very reasonable.<span class="who" style="text-align:right;padding-right:346px">Dev &amp; Kira</span></div>
  <div class="quote-dot" style="left:1146px;top:2202px">"</div>
  <div class="avatar" style="left:1146px;top:2383px;background:#5a5a5a"></div>

  <div class="dots"><span class="on"></span><span></span><span></span><span></span><span></span><span></span></div>
</section>

<section class="dreamy" role="img" aria-label="Groom kissing a smiling bride on a sunlit balcony in soft dreamy tones">
  <div class="photo-frame" style="left:140px;top:49px;width:341px;height:506px">
    <div class="ph" role="img" aria-label="Couple dancing under a lit canopy at night in dreamy edit" style="background:linear-gradient(170deg,#e9b27a,#8a4a3a 40%,#caa489 75%,#f2ddc9)"></div>
  </div>
  <div class="arrow" style="left:38px;top:280px"><svg width="12" height="12" viewBox="0 0 10 10"><path d="M7 1 2 5l5 4z" fill="#fff"/></svg></div>
  <div class="arrow" style="left:1118px;top:280px"><svg width="12" height="12" viewBox="0 0 10 10"><path d="M3 1l5 4-5 4z" fill="#fff"/></svg></div>
</section>
<div class="dreamy-script script">Colm Vance</div>
<div class="dreamy-title">DREAMY</div>

<section class="blogs">
  <h2 class="section-title abs" style="left:0;width:1200px;text-align:center;top:3243px">LATEST BLOGS</h2>
  <div class="blog-main-img" role="img" aria-label="Couple beneath illuminated stone columns at night"></div>
  <div class="abs" style="left:187px;top:3588px;width:400px">
    <div class="date">May 2, 2018</div>
    <h3 class="blog-title" style="margin-top:6px">NOAH &amp; KARINA AT THE HARBOUR<br>HALL ESTATE</h3>
    <div style="font-size:11.5px;font-weight:700;margin-top:8px">Toronto Wedding Photographer</div>
    <p style="font-size:9.5px;line-height:15.5px;color:var(--text);margin-top:18px">Noah &amp; Karina's wedding at the newish Harbour Hall Estate in Scarborough was quite possibly the wildest wedding party I have ever been to – they had a dancing robot! Now, it's ridiculously hard to describe what this entails, so just make sure you don't gloss over the party shots at the end because it is absolutely awesome.</p>
    <div class="read-more" style="margin-top:24px">Read more</div>
  </div>

  <article class="blog-item" style="top:3327px">
    <div class="thumb" role="img" aria-label="Couple inside a glass atrium" style="background:linear-gradient(160deg,#1f3a5a,#c98a3a 60%,#2a2a3a)"></div>
    <div class="info"><div class="date">September 6, 2017</div><h3 class="blog-title">ALINA &amp; COLE AT<br>MARLOW'S ON THE<br>PIER</h3><div class="read-more">Read more</div></div>
  </article>
  <article class="blog-item" style="top:3455px">
    <div class="thumb" role="img" aria-label="Couple in a golden farm field" style="background:linear-gradient(160deg,#f0b450,#9a8a3a 55%,#5a6a2a)"></div>
    <div class="info"><div class="date">July 7, 2017</div><h3 class="blog-title">SAWYER &amp; BRYNN AT<br>FIELD &amp; HEARTH FARM</h3><div class="read-more">Read more</div></div>
  </article>
  <article class="blog-item" style="top:3580px">
    <div class="thumb" role="img" aria-label="Couple on a golf course at sunset" style="background:linear-gradient(160deg,#f2c08a,#b07a4a 55%,#6a5a3a)"></div>
    <div class="info"><div class="date">July 7, 2018</div><h3 class="blog-title">ARI &amp; SHAYLA AT<br>HEATHER GLEN GOLF</h3><div class="read-more">Read more</div></div>
  </article>
  <article class="blog-item" style="top:3707px">
    <div class="thumb" role="img" aria-label="Couple by the lake at dusk with city skyline" style="background:linear-gradient(160deg,#3a4a7a,#c08a7a 55%,#2a2a4a)"></div>
    <div class="info"><div class="date">July 1, 2018</div><h3 class="blog-title">SAM &amp; ELISE AT LAKESIDE<br>PAVILION</h3><div class="read-more">Read more</div></div>
  </article>
</section>

<footer class="site-footer">
  <p>Copyright 2025 <strong>Colm Vance Photography.</strong></p>
  <span class="social" style="left:942px;background:var(--blue)"></span>
  <span class="social" style="left:985px;background:var(--blue)"></span>
</footer>

</body>
</html>
```